Wool Product Label / Yarn Band

Looking to update the packaging on our wool products. This includes a design for a paper band to place around braided wool or yarn, and a design for a sticker to place on the outside of tissue paper wrapping. Open to updating or modifying the logo, which does not fit well on a round sticker, but the sticker could also be something wool related (like a sheep or drop spindle) that does not include the logo.
Target Market(s)
Wool crafters (knitters / spinners / felters). Mainly women, aged 30-70
Industry/Entity Type
Textile
Colors
Designer to choose colors to be used in the design.
Requirements
Must have
- Band needs to include, brand name, logo, url (fernloomstead.com), dyelot number, as well as the fiber content (ex: Merino Wool) and weight of the fiber (ex: 4oz).
Nice to have
- Band would ideally be easily customized because the weight and fiber content is variable and will be printed specifically for each product, Variable information can be on a sticker or printed directly on a band that can be printed on a standard printer. Attached is a photo of the current band and it's application.

```html
<!DOCTYPE html>
<html lang="en">
<head>
<meta charset="utf-8">
<title>Fernloomstead — Yarn Band &amp; Sticker Labels</title>
<link href="https://fonts.googleapis.com/css2?family=Montserrat:wght@400;500;600&display=swap" rel="stylesheet">
<style>
  :root {
    --green: #6aab2e;
    --green-light: #a5cc52;
    --green-line: #8cc63f;
    --pattern-tint: #eef6df;
    --ink: #1d1d1b;
    --white: #ffffff;
    --rule: #e2e2e2;
  }
  * { box-sizing: border-box; margin: 0; padding: 0; }
  html, body { width: 927px; height: 1200px; overflow: hidden; background: var(--white); }
  body { position: relative; font-family: "Montserrat", Arial, sans-serif; color: var(--ink); }

  .yarn-band {
    position: absolute; left: 66px; width: 790px; height: 298px;
    border: 1px solid var(--rule); border-bottom: none; overflow: hidden; background: var(--white);
  }
  .yarn-band--green { top: 69px; }
  .yarn-band--rainbow { top: 424px; }

  .band-pattern { position: absolute; top: 0; height: 250px; background: var(--pattern-tint); }
  .band-pattern--left { left: 0; width: 221px; }
  .band-pattern--right { right: 0; width: 218px; }

  .band-footer { position: absolute; left: 0; bottom: 0; width: 100%; height: 60px; }
  .band-url {
    position: absolute; left: 0; right: 0; bottom: 14px; text-align: center;
    color: var(--white); font-size: 9.5px; letter-spacing: 3px;
  }
  .yarn-band--rainbow .band-url { bottom: 20px; font-weight: 600; font-size: 10px; letter-spacing: 3.4px; }

  .brand-mark {
    position: absolute; left: 50%; transform: translateX(-50%);
    width: 64px; height: 64px; border-radius: 50%; border: 4px solid var(--green-line);
  }
  .yarn-band .brand-mark { top: 32px; }

  .brand-name {
    position: absolute; left: 0; right: 0; text-align: center;
    color: var(--green); font-weight: 500; letter-spacing: 0.5px;
  }
  .yarn-band .brand-name { top: 108px; font-size: 34px; }

  .tagline {
    position: absolute; left: 0; right: 0; text-align: center;
    font-size: 10px; letter-spacing: 3px; font-weight: 500;
  }
  .yarn-band .tagline { top: 172px; }

  .fiber-info {
    position: absolute; left: 0; right: 0; top: 205px; text-align: center;
    font-size: 10px; font-weight: 600; word-spacing: 1px;
  }
  .fiber-info .dot {
    display: inline-block; width: 5px; height: 5px; border-radius: 50%;
    background: var(--green); margin: 0 17px 1px; vertical-align: middle;
  }

  .serial-number {
    position: absolute; left: 225px; top: 64px;
    writing-mode: vertical-rl; font-size: 7.5px; letter-spacing: 0.3px; white-space: nowrap;
  }

  .sticker { position: absolute; top: 788px; width: 332px; height: 332px; }
  .sticker--green { left: 88px; }
  .sticker--rainbow { left: 477px; }
  .sticker-ring { position: absolute; inset: 0; border-radius: 50%; }
  .sticker--green .sticker-ring { background: var(--green-light); }
  .sticker--rainbow .sticker-ring {
    background: conic-gradient(#9cc31c 0deg, #3aa53a 40deg, #3b7a6a 70deg, #6a1f86 95deg,
      #45606e 125deg, #4aa33a 150deg, #e7e800 185deg, #f9c400 215deg, #f08010 245deg,
      #e2451d 270deg, #f08a10 300deg, #f6d200 330deg, #9cc31c 360deg);
  }
  .sticker-face { position: absolute; inset: 19px; border-radius: 50%; background: var(--white); }
  .sticker-art { position: absolute; inset: 0; }
  .sticker .brand-mark { top: 62px; width: 56px; height: 56px; }
  .sticker .brand-name { top: 150px; font-size: 28px; }
  .sticker .tagline { top: 199px; font-size: 9.5px; }
  .sticker-detail { position: absolute; left: 0; right: 0; text-align: center; font-size: 9.5px; }
  .sticker-detail--fiber { top: 232px; }
  .sticker-detail--qty { top: 257px; }
  .sticker-dot {
    position: absolute; left: 50%; top: 249px; width: 4px; height: 4px; margin-left: -2px;
    border-radius: 50%; background: var(--green);
  }
</style>
</head>
<body>

  <section class="yarn-band yarn-band--green">
    <div class="band-pattern band-pattern--left" role="img" aria-label="Wavy line yarn pattern in light green"></div>
    <div class="band-pattern band-pattern--right" role="img" aria-label="Wavy line yarn pattern in light green"></div>
    <svg class="band-footer" viewBox="0 0 790 60" preserveAspectRatio="none">
      <path d="M0,6 Q31,-2 62,2 T124,4 T186,2 T248,4 T310,2 T372,4 T434,2 T496,4 T558,2 T620,4 T682,2 T744,4 T806,2 L790,60 L0,60 Z" fill="var(--green-light)"/>
    </svg>
    <div class="brand-mark"></div>
    <div class="brand-name">Fernloomstead</div>
    <div class="tagline">HAND PAINTED YARN &amp; FIBERS</div>
    <div class="fiber-info">85% Merino Wool / 15% Silk<span class="dot"></span>Qty; 4.0 oz</div>
    <div class="band-url">www.fernloomstead.com</div>
  </section>

  <section class="yarn-band yarn-band--rainbow">
    <div class="band-pattern band-pattern--left" role="img" aria-label="Wavy line yarn pattern in light green"></div>
    <div class="band-pattern band-pattern--right" role="img" aria-label="Wavy line yarn pattern in light green"></div>
    <svg class="band-footer" viewBox="0 0 790 60" preserveAspectRatio="none">
      <defs>
        <linearGradient id="rainbow-band" x1="0" x2="1" y1="0" y2="0">
          <stop offset="0" stop-color="#e2451d"/>
          <stop offset="0.2" stop-color="#f8b000"/>
          <stop offset="0.3" stop-color="#fbea00"/>
          <stop offset="0.5" stop-color="#9cc31c"/>
          <stop offset="0.7" stop-color="#3fa535"/>
          <stop offset="0.88" stop-color="#3b6e72"/>
          <stop offset="1" stop-color="#6a2b80"/>
        </linearGradient>
      </defs>
      <path d="M0,6 Q31,-2 62,2 T124,4 T186,2 T248,4 T310,2 T372,4 T434,2 T496,4 T558,2 T620,4 T682,2 T744,4 T806,2 L790,60 L0,60 Z" fill="url(#rainbow-band)"/>
    </svg>
    <div class="serial-number">S/N: MER/SILK-BLEND1</div>
    <div class="brand-mark"></div>
    <div class="brand-name">Fernloomstead</div>
    <div class="tagline">HAND PAINTED YARN &amp; FIBERS</div>
    <div class="fiber-info">85% Merino Wool / 15% Silk<span class="dot"></span>Qty; 4.0 oz</div>
    <div class="band-url">www.fernloomstead.com</div>
  </section>

  <section class="sticker sticker--green">
    <div class="sticker-ring" role="img" aria-label="Ring of wavy yarn lines in green"></div>
    <div class="sticker-face"></div>
    <svg class="sticker-art" viewBox="0 0 332 332">
      <path d="M80,272 A139,139 0 1 1 252,272" fill="none" stroke="var(--green-line)" stroke-width="1"/>
      <path id="url-arc-green" d="M40,166 A126,126 0 0 0 292,166" fill="none"/>
      <text font-size="10.5" letter-spacing="2.6" fill="var(--ink)"><textPath href="#url-arc-green" startOffset="50%" text-anchor="middle">www.fernloomstead.com</textPath></text>
    </svg>
    <div class="brand-mark"></div>
    <div class="brand-name">Fernloomstead</div>
    <div class="tagline">HAND PAINTED YARN &amp; FIBERS</div>
    <div class="sticker-detail sticker-detail--fiber">85% Merino Wool / 15% Silk</div>
    <div class="sticker-dot"></div>
    <div class="sticker-detail sticker-detail--qty">Qty; 4.0 oz</div>
  </section>

  <section class="sticker sticker--rainbow">
    <div class="sticker-ring" role="img" aria-label="Ring of wavy yarn lines in rainbow colours"></div>
    <div class="sticker-face"></div>
    <svg class="sticker-art" viewBox="0 0 332 332">
      <path d="M80,272 A139,139 0 1 1 252,272" fill="none" stroke="var(--green-line)" stroke-width="1"/>
      <path id="url-arc-rainbow" d="M40,166 A126,126 0 0 0 292,166" fill="none"/>
      <text font-size="10.5" letter-spacing="2.6" fill="var(--ink)"><textPath href="#url-arc-rainbow" startOffset="50%" text-anchor="middle">www.fernloomstead.com</textPath></text>
    </svg>
    <div class="brand-mark"></div>
    <div class="brand-name">Fernloomstead</div>
    <div class="tagline">HAND PAINTED YARN &amp; FIBERS</div>
    <div class="sticker-detail sticker-detail--fiber">85% Merino Wool / 15% Silk</div>
    <div class="sticker-dot"></div>
    <div class="sticker-detail sticker-detail--qty">Qty; 4.0 oz</div>
  </section>

</body>
</html>
```